Travinex - You are the Boss!

Travinex is a new Silicon Valley company, of the pelim founders from Berlin, which provides a "Shared Pioneer Circle". This platform allows the crowd to support startups with money, experts and fame. Our Vision is, that everyone should become an entrepreneur.

Pls find all brief details in the attached document
Updates

Would be nice to have a list of more social services I'm available on, like a list of pictograms of all my services:

Find me on: vooka, bramlet+, qrt, fenwix, moodrail, zupp, hvoxa, etc...

pls make sure to use the right font:
http://www.typemarlow.com/fonts/Velquin

Target Market(s)

Main target market is those already involved in the startup industry, by fundraising, investing, advising, cofounding and working. Travinex brings a totaly new transparency and collaborative way of starting companies to that business.

· Entrepreneurs (looking for funding, team and community)
· Investors (looking for hot investments and )
· Experts (workers looking for startups they can work for equity)
· Incubators & Business Schools (looking for tools to advise startups)

Industry/Entity Type

It Company

Requirements
Must have
• Pls find all brief details in the attached document
Nice to have

```html
<!DOCTYPE html>
<html lang="en">
<head>
<meta charset="utf-8">
<title>Travinex – Business Card</title>
<link rel="stylesheet" href="https://fonts.googleapis.com/css2?family=Arimo:wght@400;700&family=Audiowide&display=swap">
<style>
  :root {
    --page-bg: #e9e4dd;
    --card-deep: #05060c;
    --card-navy: #1b2a6b;
    --band-teal: #1a8f9a;
    --ufo-orange: #ef6a3f;
    --ufo-navy: #0e1433;
    --text-white: #ffffff;
    --text-soft: #e6e9f4;
    --title-grey: #d9dbe2;
    --icon-teal: #27a3ad;
  }
  * { margin: 0; padding: 0; box-sizing: border-box; }
  html, body { width: 1200px; height: 900px; overflow: hidden; }
  body {
    background: var(--page-bg);
    position: relative;
    font-family: "Arimo", Arial, sans-serif;
    color: var(--text-white);
  }
  .card {
    position: absolute;
    top: 269px;
    width: 550px;
    height: 314px;
    border-radius: 16px;
    overflow: hidden;
    background:
      radial-gradient(ellipse 55% 90% at 55% 10%, rgba(46,68,160,0.85), rgba(27,42,107,0.2) 60%, transparent 80%),
      linear-gradient(180deg, #0a0f26 0%, var(--card-deep) 100%);
    box-shadow: 0 6px 14px rgba(0,0,0,0.25);
  }
  .card--front { left: 29px; }
  .card--back {
    left: 625px;
    background:
      radial-gradient(ellipse 60% 95% at 60% 20%, rgba(46,68,160,0.8), rgba(27,42,107,0.25) 60%, transparent 85%),
      linear-gradient(180deg, #0a0f26 0%, var(--card-deep) 100%);
  }
  .card__band {
    position: absolute; left: 0; right: 0; bottom: 0; height: 19px;
    background: var(--band-teal);
  }
  .card__stars { position: absolute; inset: 0; }

  /* front */
  .ufo-art {
    position: absolute; left: 276px; top: 30px; width: 194px; height: 92px;
    border-radius: 50% / 60%;
    background: radial-gradient(ellipse at 50% 40%, #f47a50, var(--ufo-orange) 60%, #c9532e);
  }
  .brand-name {
    position: absolute; left: 288px; top: 134px;
    font-weight: 700; font-size: 31px; letter-spacing: 0.5px;
    color: var(--title-grey);
  }
  .tagline {
    position: absolute; right: 24px; top: 182px;
    font-weight: 700; font-size: 14px;
  }
  .holder { position: absolute; left: 33px; top: 155px; }
  .holder__name { font-weight: 700; font-size: 14px; }
  .holder__role { font-size: 11px; color: var(--text-soft); margin-top: 3px; }
  .contacts {
    position: absolute; left: 33px; top: 206px; list-style: none;
    font-size: 13px; line-height: 18px; color: var(--text-soft);
  }
  .contacts li { display: flex; align-items: center; gap: 8px; }
  .contacts svg { width: 10px; height: 10px; flex: none; }
  .website {
    position: absolute; right: 24px; top: 276px;
    font-size: 13px; color: var(--text-soft);
  }

  /* back */
  .pitch__title {
    position: absolute; left: 37px; top: 14px;
    font-family: "Audiowide", "Arimo", sans-serif;
    font-size: 29px; color: var(--title-grey);
  }
  .pitch__list {
    position: absolute; left: 37px; top: 60px; list-style: none;
    font-family: "Audiowide", "Arimo", sans-serif;
    font-size: 14.5px; line-height: 19px;
  }
  .pitch__list li { display: flex; align-items: center; gap: 6px; }
  .pitch__bullet {
    width: 17px; height: 7px; border-radius: 50%;
    background: var(--icon-teal); flex: none;
  }
  .pitch__join {
    position: absolute; left: 43px; top: 123px;
    font-family: "Audiowide", "Arimo", sans-serif; font-size: 14.5px;
  }
  .ufo-art--large {
    left: 217px; top: 160px; width: 330px; height: 150px;
    border-radius: 50% / 55%;
  }
  .website--spaced {
    left: 26px; right: auto; top: 271px;
    letter-spacing: 3px; font-size: 13px;
  }
</style>
</head>
<body>

<section class="card card--front" aria-label="Card front">
  <svg class="card__stars" width="550" height="314" aria-hidden="true">
    <g fill="#ffffff">
      <circle cx="70" cy="36" r="1.3"/><circle cx="95" cy="50" r="1"/><circle cx="140" cy="75" r="1"/>
      <circle cx="203" cy="80" r="1.2"/><circle cx="188" cy="120" r="1"/><circle cx="150" cy="95" r="1"/>
      <circle cx="490" cy="35" r="1.2"/><circle cx="520" cy="60" r="1"/><circle cx="440" cy="105" r="1.3"/>
      <circle cx="505" cy="115" r="1"/><circle cx="470" cy="155" r="1"/><circle cx="110" cy="110" r="1"/>
    </g>
  </svg>
  <div class="ufo-art" role="img" aria-label="Orange flying saucer illustration"></div>
  <div class="brand-name">Travinex</div>
  <div class="tagline">You are the Boss!</div>
  <div class="holder">
    <div class="holder__name">Lukas Brenner</div>
    <div class="holder__role">Founder and CEO</div>
  </div>
  <ul class="contacts">
    <li><svg viewBox="0 0 10 10" aria-hidden="true"><rect x="2.5" y="0.5" width="5" height="9" rx="1" fill="var(--icon-teal)"/></svg>0300 4417</li>
    <li><svg viewBox="0 0 10 10" aria-hidden="true"><rect x="0.5" y="2" width="9" height="6.5" fill="none" stroke="var(--icon-teal)"/><path d="M0.5 2 L5 6 L9.5 2" fill="none" stroke="var(--icon-teal)"/></svg>lb@travinex.com</li>
    <li><svg viewBox="0 0 10 10" aria-hidden="true"><rect width="10" height="10" rx="1.5" fill="var(--icon-teal)"/></svg>/lukasbrenner</li>
    <li><svg viewBox="0 0 10 10" aria-hidden="true"><rect width="10" height="10" rx="1.5" fill="var(--icon-teal)"/></svg>/lukasbrenner</li>
    <li><svg viewBox="0 0 10 10" aria-hidden="true"><rect width="10" height="10" rx="1.5" fill="var(--icon-teal)"/></svg>/in/lukasbrenner</li>
  </ul>
  <div class="website">www.travinex.com</div>
  <div class="card__band"></div>
</section>

<section class="card card--back" aria-label="Card back">
  <svg class="card__stars" width="550" height="314" aria-hidden="true">
    <g fill="#ffffff">
      <circle cx="45" cy="190" r="1.2"/><circle cx="60" cy="215" r="1"/><circle cx="150" cy="230" r="1"/>
      <circle cx="172" cy="250" r="1.2"/><circle cx="183" cy="215" r="1"/><circle cx="255" cy="150" r="1"/>
      <circle cx="470" cy="50" r="1"/><circle cx="510" cy="120" r="1.2"/><circle cx="395" cy="175" r="1"/>
      <circle cx="520" cy="170" r="1"/><circle cx="90" cy="175" r="1"/>
    </g>
  </svg>
  <h2 class="pitch__title">Are you interested in?</h2>
  <ul class="pitch__list">
    <li><span class="pitch__bullet"></span>Starting your own Business?</li>
    <li><span class="pitch__bullet"></span>Investing in hot Startups?</li>
    <li><span class="pitch__bullet"></span>Working for the next “Chatterly”?</li>
  </ul>
  <div class="pitch__join">Join us on Chatterly.com/Travinex</div>
  <div class="ufo-art ufo-art--large" role="img" aria-label="Large orange flying saucer illustration"></div>
  <div class="website website--spaced">www.travinex.com</div>
  <div class="card__band"></div>
</section>

</body>
</html>
```